Bed & Breakfast Wordpress Theme - Design Only

We are looking for a Wordpress theme for an award winning UK Bed & Breakfast (Guesthouse) www.fernbrookhouse.co.uk
You will see that the current site is basic and dated, we need a new site that showcases the very high standard of rooms on offer and is geared towards both mobile and desktop browsing.
We would like the colours that have been used in the rooms and building (as seen on the current website) to feature in the design.
We particularly like the look of this accommodation provider website: http://www.wrenmeadowbarns.co.uk
Selected website images can be downloaded here, feel free to use more from the existing website too:
https://www.filevaultly.com/s/qa7mr41xt8zv2kp/website%20images.zip
Target Market(s)
The accommodation is upmarket and the design needs to subtly communicate this.
The accommodation attracts a varied mix of ages so needs to be up scale without being overly modern.
Industry/Entity Type
Accommodation
Requirements
Must have
- As the accommodation does not have a logo we need a basic typographic logo incorporated into the design.
Colours of the building and rooms must be integrated into the design in some way.
A bold homepage that allows images of the rooms on offer and key information to be visibale above the fold. The goal of the homepage is for someone to then click Rooms or Prices so calls to action may help here.
Separate designs for a sidebar and full width version of sub pages.
An area that shows off the awards won by the company on all pages and space for testimonials.
The site must enable an easy transition from - homepage - to rooms - to prices with possible call to action buttons in the top right corner on these pages
The site needs to have a Homepage layout, a general sub page layout, and a 'Rooms' page layout which will showcase all rooms available possibly in a grid layout.
Nice to have
- Please use some of the images available currently on the website in your mockup, particularly of the building and rooms.
Should not have
- No need for any type of booking fields or engine as the booking system will be embedded on a full width page.

```html
<!DOCTYPE html>
<html lang="en">
<head>
<meta charset="utf-8">
<title>Fernbrook House – A small and friendly hotel</title>
<link href="https://fonts.googleapis.com/css2?family=PT+Sans:wght@400;700&family=Arimo:wght@400;700&family=Roboto+Condensed:wght@400&display=swap" rel="stylesheet">
<style>
  :root{
    --olive:#8e9367;
    --olive-nav:#9a9e7a;
    --olive-active:#aaae8d;
    --ink:#3a3a3a;
    --muted:#555;
    --grey-icon:#8a8a8a;
    --teal:#5f9b90;
    --footer:#3e3e3e;
    --footer-line:#5a5a5a;
    --white:#fff;
  }
  *{box-sizing:border-box;margin:0;padding:0}
  html,body{width:842px;height:1200px;overflow:hidden;background:var(--white)}
  body{position:relative;font-family:"Arimo",Arial,sans-serif;color:var(--ink)}
  .abs{position:absolute}

  /* header */
  .social{left:518px;top:16px;display:flex;gap:11px}
  .social span{width:23px;height:23px;border-radius:50%;background:var(--grey-icon);display:block}
  .brand{left:60px;top:46px;font-family:"PT Sans",sans-serif;font-size:27px;color:var(--olive)}
  .tagline{left:61px;top:81px;font-family:"PT Sans",sans-serif;font-size:11px;color:var(--muted)}
  .contact{font-family:"PT Sans",sans-serif;font-size:11px;color:var(--ink);display:flex;align-items:center;gap:7px}
  .contact svg{fill:var(--grey-icon)}
  .c-phone{left:521px;top:59px}
  .c-mail{left:642px;top:59px}
  .c-addr{left:521px;top:86px}

  /* nav */
  .nav{left:60px;top:115px;width:720px;height:45px;background:var(--olive-nav);display:flex;font-size:12px;color:var(--white);letter-spacing:.3px}
  .nav a{display:flex;align-items:center;padding:0 21px;color:inherit;text-decoration:none}
  .nav a.active{background:var(--olive-active);padding:0 23px}
  .nav a:nth-child(2){padding-left:21px}

  /* hero */
  .hero{left:60px;top:160px;width:720px;height:275px;background:linear-gradient(180deg,#b9c3c9 0%,#e7e5dc 30%,#d9d6cc 60%,#5f5a4a 85%,#3d3b33 100%)}
  .hero-bar{left:60px;top:384px;width:720px;height:51px;background:rgba(30,30,30,.55)}
  .hero-title{left:77px;top:403px;font-size:15px;color:var(--white);letter-spacing:.2px}
  .btn{height:25px;display:flex;align-items:center;justify-content:center;font-size:12px;color:var(--white);border:1px solid rgba(255,255,255,.25)}
  .btn-book{left:490px;top:400px;width:106px;background:var(--teal)}
  .btn-find{left:614px;top:400px;width:78px;background:#4a4a4a}
  .dots{left:726px;top:410px;display:flex;gap:2px}
  .dots i{width:8px;height:8px;border-radius:50%;border:1px solid #ddd;display:block}
  .dots i.on{background:#ddd}

  /* welcome */
  .h-section{font-family:"Roboto Condensed",sans-serif;font-size:14px;color:var(--olive)}
  .h-welcome{left:59px;top:467px}
  .h-video{left:533px;top:467px}
  .welcome{left:59px;top:503px;width:425px;font-size:9.6px;line-height:16px;color:var(--ink)}
  .welcome p+p{margin-top:8px}
  .video{left:535px;top:506px;width:245px;height:148px;background:linear-gradient(160deg,#6a6a6a,#2e2e2e 70%);box-shadow:0 1px 3px rgba(0,0,0,.4)}
  .video-play{left:636px;top:552px}
  .video-ctrl{left:535px;top:635px;width:245px;height:19px;background:#1d1d1d;display:flex;align-items:center;font-size:6.5px;color:#ddd;padding:0 6px;gap:6px}
  .track{flex:1;height:3px;background:#555;position:relative}
  .track b{position:absolute;left:0;top:0;width:50%;height:3px;background:#c22}

  /* feature cards */
  .card{top:710px;width:217px;height:203px;background:var(--white);box-shadow:0 0 3px rgba(0,0,0,.25)}
  .card-img{position:absolute;left:6px;top:6px;width:205px;height:105px}
  .card h3{position:absolute;left:9px;top:124px;font-size:12.5px;font-weight:700;color:var(--olive)}
  .card p{position:absolute;left:9px;top:146px;width:204px;font-size:9.4px;line-height:15px;color:var(--muted)}
  .card-1{left:61px}.card-2{left:313px}.card-3{left:565px}
  .img-house{background:linear-gradient(180deg,#8fa8c0 0%,#ecebe6 35%,#d8d6cf 70%,#4b5338 100%)}
  .img-tour{background:linear-gradient(180deg,#6a5a2e 0%,#d6c58e 40%,#b79b58 75%,#3e3522 100%)}
  .img-nature{background:linear-gradient(180deg,#d9c7a0 0%,#b79867 60%,#8a6a3e 100%)}

  /* footer */
  .footer{left:0;top:950px;width:842px;height:250px;background:var(--footer)}
  .f-head{top:976px;font-size:13.5px;font-weight:700;color:var(--white)}
  .f-test{left:61px}.f-find{left:367px}.f-awards{left:590px}
  .quote{left:75px;top:1012px;width:262px;font-size:9.8px;line-height:17.7px;color:var(--white)}
  .qmark{font-family:Georgia,serif;color:#888;font-size:14px}
  .q-open{left:61px;top:1005px}
  .cite{left:177px;top:1092px;font-family:"PT Sans",sans-serif;font-size:10px;color:var(--white)}
  .map{left:367px;top:1008px;width:179px;height:95px;background:linear-gradient(135deg,#e9e6dc,#d7dccb 60%,#cfd6e2)}
  .badge-a{left:590px;top:1008px;width:127px;height:54px;background:#8d8d8d}
  .badge-b{left:730px;top:1008px;width:44px;height:67px;background:#9a8f7a}
  .badge-c{left:593px;top:1070px;width:60px;height:60px;border-radius:50%;background:#1d2c6b;border:2px solid #c7c7c7}
  .f-rule{left:60px;top:1154px;width:720px;height:1px;background:var(--footer-line)}
  .copy{left:60px;top:1172px;font-family:"PT Sans",sans-serif;font-size:11px;color:var(--white)}
</style>
</head>
<body>

<header>
  <div class="abs social" aria-label="Social links"><span></span><span></span><span></span><span></span></div>
  <div class="abs brand">Fernbrook House</div>
  <div class="abs tagline">A Small and friendly hotel.</div>

  <div class="abs contact c-phone">
    <svg width="10" height="14" viewBox="0 0 10 14"><path d="M2 1c1-.6 2 0 2 .8L3.5 4c-.2.7-1 .8-1 1.6 0 1.6 1 3.5 2 4.3.5.4 1 0 1.6-.2l1.8.7c.6.5.4 1.5-.4 2C5.8 13.5 1 10 1 5 1 3 1.2 1.5 2 1z"/></svg>
    903-555-0142
  </div>
  <div class="abs contact c-mail">
    <svg width="14" height="10" viewBox="0 0 14 10"><path d="M.5.5h13v9H.5z" fill="none" stroke="#8a8a8a"/><path d="M.5.5 7 6l6.5-5.5" fill="none" stroke="#8a8a8a"/></svg>
    info@fernbrookhouse.co.uk
  </div>
  <div class="abs contact c-addr">
    <svg width="11" height="15" viewBox="0 0 11 15"><path d="M5.5 0A5.5 5.5 0 0 0 0 5.5C0 9.5 5.5 15 5.5 15S11 9.5 11 5.5A5.5 5.5 0 0 0 5.5 0z"/></svg>
    4820 Alder Crest&nbsp; #210 Elm Valley, CA 95612
  </div>
</header>

<nav class="abs nav">
  <a class="active" href="#">HOME</a>
  <a href="#">ROOMS</a>
  <a href="#">PRICES</a>
  <a href="#">PICTURE GALLERY</a>
  <a href="#">INFORMATION</a>
  <a href="#">SITEMAP</a>
  <a href="#">CONTACT</a>
</nav>

<section>
  <div class="abs hero" role="img" aria-label="White-painted guesthouse with a yellow front door, climbing plants and a parked car"></div>
  <div class="abs hero-bar"></div>
  <div class="abs hero-title">DUIS AUTEM VEL EUM IRIURE DOLOR IN HENDRERIT</div>
  <div class="abs btn btn-book">BOOK ONLINE</div>
  <div class="abs btn btn-find">FIND US</div>
  <div class="abs dots"><i class="on"></i><i></i><i></i><i></i></div>
</section>

<section>
  <h2 class="abs h-section h-welcome">WELCOME TO OUR WEBSITE</h2>
  <div class="abs welcome">
    <p>Duis autem vel eum iriure dolor in hendrerit in vulputate velit esse molestie consequat, vel illum dolore eu feugiat nulla facilis.&nbsp; Typi non habent claritatem.</p>
    <p>Duis autem vel eum iriure dolor in hendrerit in vulputate velit esse molestie consequat, vel illum dolore eu feugiat nulla facilisis at vero eros et accumsan et iusto odio dignissim qui blandit praesent luptatum zzril delenit augue duis dolore te feugait nilla facilisi. Claritas est etiam process us dynamicus, qui sequitur mutationem consuetudium lectorum. Mirum est notare quam littera gothica quam nunc putamus parum claram, anteposuerit litterarum formas humanitatis Claritas est etiam processus dynamicus, qui sequitur mutationem consuetudium&nbsp; quam nunc putamius parum claram, anteposuerit litterarum formas</p>
  </div>

  <h2 class="abs h-section h-video">WREN VALE VIDEO</h2>
  <div class="abs video" role="img" aria-label="Video still of a guesthouse dining room with chairs and table"></div>
  <svg class="abs video-play" width="40" height="40" viewBox="0 0 40 40"><circle cx="20" cy="20" r="19" fill="rgba(0,0,0,.25)"/><path d="M15 11l13 9-13 9z" fill="#d8d8d8"/></svg>
  <div class="abs video-ctrl">
    <svg width="5" height="6" viewBox="0 0 5 6"><path d="M0 0l5 3-5 3z" fill="#ddd"/></svg>
    <div class="track"><b></b></div>
    <span>1:26 / 3:22</span>
    <svg width="6" height="6" viewBox="0 0 6 6"><path d="M0 2h2l3-2v6L2 4H0z" fill="#ddd"/></svg>
    <span style="width:14px;height:2px;background:#c22;display:block"></span>
    <b style="font-style:italic">HD</b>
  </div>
</section>

<section>
  <article class="abs card card-1">
    <div class="card-img img-house" role="img" aria-label="Front of the white guesthouse with a yellow door"></div>
    <h3>Special Offers</h3>
    <p>Claritas est etiam processus dynamicus, qui sequitur mutationem consuetudium lectorum.M irum est notare quam littera gothica, quam.</p>
  </article>
  <article class="abs card card-2">
    <div class="card-img img-tour" role="img" aria-label="Virtual tour panorama of a warmly lit interior"></div>
    <h3>Virtual Tour</h3>
    <p>Claritas est etiam processus dynamicus, qui sequitur mutationem consuetudium lectorum.M irum est notare quam littera gothica, quam.</p>
  </article>
  <article class="abs card card-3">
    <div class="card-img img-nature" role="img" aria-label="Stag standing in misty golden woodland"></div>
    <h3>Our Environment</h3>
    <p>Claritas est etiam processus dynamicus, qui sequitur mutationem consuetudium lectorum.M irum est notare quam littera gothica, quam.</p>
  </article>
</section>

<footer>
  <div class="abs footer"></div>
  <h4 class="abs f-head f-test">Testimonials</h4>
  <h4 class="abs f-head f-find">Find us</h4>
  <h4 class="abs f-head f-awards">Awards</h4>

  <span class="abs qmark q-open">&ldquo;</span>
  <p class="abs quote">Maecenas sit amet tincidunt elit. Pellentesque habitaque senectuset netus et malesuada fams ac turpisiegei Nulla facilisi. Nulla facilisi. Pellentesque habitant morbi trisque. Duis auten vel eum iriure dolor. Typi non habent. <span class="qmark">&rdquo;</span></p>
  <div class="abs cite">- Helen Marsh, Company Name</div>

  <div class="abs map" role="img" aria-label="Street map showing the guesthouse location"></div>

  <div class="abs badge-a" role="img" aria-label="Tourism award badge"></div>
  <div class="abs badge-b" role="img" aria-label="Excellence award badge"></div>
  <div class="abs badge-c" role="img" aria-label="Local quality mark badge"></div>

  <div class="abs f-rule"></div>
  <div class="abs copy">Copyright © 2013. All Rights Reserved.</div>
</footer>

</body>
</html>
```